TQ Regulatory Partners - Biz Card - Re-do

I would like a re-do on my business card.

See my Internet site - tqregpartners.com

1) Remove direct phone line.
2) Add company moto - integrity, diligence, and excellence
3) Add Consulting Services listing:
-Benefit Technology
-ERISA Compliance
-Contract/Vendor Management
-Human Resource/Payroll
-Medical/Prescription Drug
-Integrated Leave of Absence

Target Market(s)

Employee benefit consulting and insurance purchasers, Usually human resource executives

Industry/Entity Type

Human Resource

Contact Information for Business Card

Same business card color scheme, logo,

Font styles to use
Sans Serif

Requirements
Must have
• Same color scheme and logo. Remove direct phone number. Keep all numbers, internet address.

```html
<!DOCTYPE html>
<html lang="en">
<head>
<meta charset="utf-8">
<title>TQ Regulatory Partners – Business Card</title>
<link href="https://fonts.googleapis.com/css2?family=Lato:wght@400;700&display=swap" rel="stylesheet">
<style>
  :root {
    --plum: #6b1f45;
    --slate: #5e5f62;
    --slate-dark: #4a4b4e;
    --ink: #58595b;
    --paper: #ffffff;
    --backdrop: #e9e9ea;
  }
  * { box-sizing: border-box; margin: 0; padding: 0; }
  html, body { width: 1200px; height: 900px; overflow: hidden; }
  body {
    background: var(--backdrop);
    font-family: "Lato", sans-serif;
    display: flex; align-items: center; justify-content: center; gap: 30px;
  }
  .card {
    position: relative; width: 560px; height: 320px;
    border-radius: 14px; overflow: hidden;
    box-shadow: 0 6px 18px rgba(0,0,0,.12);
  }

  /* Back */
  .card--back { background: var(--slate); color: var(--paper); }
  .card--back .brand {
    position: absolute; top: 56px; left: 0; right: 0; text-align: center;
  }
  .brand__dot {
    width: 58px; height: 58px; border-radius: 50%; background: var(--plum);
    margin: 0 auto 14px;
  }
  .brand__name { font-size: 30px; font-weight: 400; letter-spacing: .3px; }
  .brand__motto { font-size: 15px; margin-top: 6px; letter-spacing: .4px; }
  .services {
    position: absolute; left: 28px; right: 28px; bottom: 30px;
    display: flex; justify-content: space-between; list-style: none;
  }
  .services ul { list-style: none; }
  .services li {
    font-size: 12.5px; line-height: 1.55; padding-left: 12px; position: relative;
  }
  .services li::before {
    content: ""; position: absolute; left: 0; top: 7px;
    width: 6px; height: 6px; border-radius: 50%; background: var(--plum);
  }
  .card--back .stripe {
    position: absolute; left: 0; right: 0; bottom: 0; height: 8px; background: var(--plum);
  }

  /* Front */
  .card--front { background: var(--paper); color: var(--ink); }
  .card--front .brand {
    position: absolute; top: 44px; left: 270px; display: flex; align-items: center; gap: 16px;
  }
  .card--front .brand__dot { width: 84px; height: 84px; margin: 0; }
  .card--front .brand__name { font-size: 27px; line-height: 1.1; color: var(--ink); }
  .divider {
    position: absolute; left: 250px; right: 26px; top: 188px; height: 1px; background: var(--ink);
  }
  .person { position: absolute; left: 38px; top: 170px; }
  .person__name { font-size: 26px; font-weight: 700; color: var(--plum); }
  .person__title { font-size: 14px; margin-top: 2px; }
  .contacts { position: absolute; left: 38px; top: 236px; list-style: none; }
  .contacts li { display: flex; align-items: center; gap: 10px; font-size: 13.5px; line-height: 1.45; }
  .contacts svg { width: 12px; height: 12px; fill: var(--plum); flex: none; }
  .address {
    position: absolute; right: 34px; top: 204px; font-size: 13px; line-height: 1.4; text-align: left;
  }
  .tab { position: absolute; left: 0; top: 174px; width: 8px; height: 36px; background: var(--plum); }
  .base { position: absolute; left: 0; right: 0; bottom: 0; height: 8px; display: flex; }
  .base__grey { flex: 0 0 72%; background: var(--slate); }
  .base__plum { flex: 1; background: var(--plum); margin-left: 4px; }
</style>
</head>
<body>

  <section class="card card--back">
    <div class="brand">
      <div class="brand__dot"></div>
      <div class="brand__name">TQ Regulatory Partners</div>
      <div class="brand__motto">Integrity, Diligence, and Excellence</div>
    </div>
    <div class="services">
      <ul><li>Benefit Technology</li><li>ERISA Compliance</li></ul>
      <ul><li>Contract/Vendor Management</li><li>Human Resource/Payroll</li></ul>
      <ul><li>Medical/Prescription Drug</li><li>Integrated Leave of Absence</li></ul>
    </div>
    <div class="stripe"></div>
  </section>

  <section class="card card--front">
    <div class="brand">
      <div class="brand__dot"></div>
      <div class="brand__name">TQ Regulatory<br>Partners</div>
    </div>
    <div class="divider"></div>
    <div class="tab"></div>
    <div class="person">
      <div class="person__name">Daniel Hargrove</div>
      <div class="person__title">President</div>
    </div>
    <ul class="contacts">
      <li><svg viewBox="0 0 24 24"><path d="M6.6 10.8a15 15 0 0 0 6.6 6.6l2.2-2.2c.3-.3.7-.4 1-.2 1.1.4 2.3.6 3.6.6.6 0 1 .4 1 1V20c0 .6-.4 1-1 1A17 17 0 0 1 3 4c0-.6.4-1 1-1h3.5c.6 0 1 .4 1 1 0 1.3.2 2.5.6 3.6.1.3 0 .7-.2 1z"/></svg>555.210.4471</li>
      <li><svg viewBox="0 0 24 24"><path d="M6 2h12v6H6zM4 9h16a2 2 0 0 1 2 2v6h-4v5H6v-5H2v-6a2 2 0 0 1 2-2zm4 8v3h8v-3z"/></svg>555.210.4472</li>
      <li><svg viewBox="0 0 24 24"><path d="M2 5h20v14H2zm2 2v.5l8 5 8-5V7z"/></svg>dhargrove@tqregpartners.com</li>
      <li><svg viewBox="0 0 24 24"><path d="M12 2a10 10 0 1 0 0 20 10 10 0 0 0 0-20zm6.9 9h-3a15 15 0 0 0-1.3-5.9A8 8 0 0 1 18.9 11zM12 4c.9 1.2 1.8 3.7 1.9 7h-3.8c.1-3.3 1-5.8 1.9-7zM9.4 5.1A15 15 0 0 0 8.1 11h-3a8 8 0 0 1 4.3-5.9zM5.1 13h3a15 15 0 0 0 1.3 5.9A8 8 0 0 1 5.1 13zM12 20c-.9-1.2-1.8-3.7-1.9-7h3.8c-.1 3.3-1 5.8-1.9 7zm2.6-1.1a15 15 0 0 0 1.3-5.9h3a8 8 0 0 1-4.3 5.9z"/></svg>www.tqregpartners.com</li>
    </ul>
    <address class="address" style="font-style:normal">
      180 Harbor Street NE<br>Suite 300, Lakeview<br>MI 49010
    </address>
    <div class="base"><div class="base__grey"></div><div class="base__plum"></div></div>
  </section>

</body>
</html>
```